Lena Hartwell Web

Lena Hartwell is a singer/songwriter that has a presence in the market for over 20 years. She currently has a website, lenahartwell.example that needs a major makeover. IT needs to be reorganized to; 1) make it more user friendly; 2) enable multi-languages including; Spanish, French, Russian, Japanese, Chinese and Portuguese; 3) enable purchases online through a storefront of promotional merchandise and music tracks. She has a logo that needs an update, as well as we currently have a business card open on PixelBazaar for input. Working to re-brand, or refresh her brand.

Lena Hartwell is the next Rosa Delmont! She has 5 platinum records, Lumen Award nominations and tours with Harold Prescott globally and is Nora Vandermeer's key backup singer for 12 years.
Updates

Some common questions have come up.  Here is some further input:

1) Colors - No specific color in mind but probably earth tones.  Although at this point we''re completely open.  Mary likes classical style, Russian, French decor.  Paris architecture. Greek, Italian textures, Goddess like symbols from the Roman Empire, or the symbols and pomp of the British monarchy.  One name on tap for the new CD is "Lanterns Over Quiet Water"
2) Example website - I have not found a new one specifically, but what I don''t like about the existing one is it is not easy to navigate.  Needs to be streamlined and easy to navigate with a storefront for merchandise and music downloads.  
3) On Logo - We''re revamping a "Global" merchandise rollout logo.  We''ve also considered possibly modifying the old english "Hartwell" family crest which signifies royalty, but have not explored that too much.  The hexagon yellow logo on her current website, I was thinking of modifying to gold (brushed - or polished?), then taking the LH lettering using a fountain pen type look there the line thickness flows with pressure on the pen, then make the gold look like a pillow, with the letter making an impression into the gold pillow.  This expands to a high quality pin, blinged up broach with diamonds imbedded for example, Global label identity, tee shirts, label tag on fashion clothing etc etc. 
 4) One thing marketing has asked us to build is a routine video blog to reach out to fans in a personal way.  Short clips of daily activity, travel prep for shows, etc. Possibly a signup/fanpage where people get emails sent back whenever anything new is posted, like a video blog, new pics, new events.  A menu to choose what you get updates on. 

Thanks, Dennis

Target Market(s)

1) Fan base in Europe, Asia, Latin America and North America
2) Movie producers seeking soundtracks
3) Private clients seeking an outstanding performer for corporate events

Industry/Entity Type

Singer

Requirements
Must have
• Better organization into smaller pages. Items critical include: 1) music tracks, 2) ClipStream links, 3) photos & Video, 4) storefront to enable online merchandise purchase 5) a way to illustrate her genre from; gospel, to rock, funk, R&B, country,

```html
<!DOCTYPE html>
<html lang="en">
<head>
<meta charset="utf-8">
<title>Lena Hartwell — Official Site</title>
<link rel="stylesheet" href="https://fonts.googleapis.com/css2?family=PT+Sans+Narrow:wght@700&family=Open+Sans:wght@400;600&display=swap">
<style>
:root{
  --gold:#fdc72f;
  --gold-deep:#f2b01e;
  --navy:#1e2a4f;
  --ink:#222631;
  --text:#3a3a3a;
  --muted:#5b5b5b;
  --page:#ececec;
  --card:#f4f4f4;
  --price:#f0a81a;
  --footer-top:#2c3a78;
  --footer-bottom:#1c2552;
  --footer-base:#1a2148;
  --white:#ffffff;
}
*{margin:0;padding:0;box-sizing:border-box}
html,body{width:1200px;height:2387px;overflow:hidden}
body{background:var(--page);font-family:"Open Sans",Arial,sans-serif;color:var(--text);position:relative}
.heading{font-family:"PT Sans Narrow","Arial Narrow",sans-serif;font-weight:700;text-transform:uppercase;color:var(--ink)}
.abs{position:absolute}

/* hero */
.hero-backdrop{left:0;top:0;width:1200px;height:490px;background:linear-gradient(135deg,#5a3a14 0%,#b07a2c 35%,#7b5220 60%,#caa055 85%,#6d4716 100%)}
.main-nav{left:91px;top:91px;width:1018px;height:60px;background:linear-gradient(#ffd24a,var(--gold-deep));display:flex;justify-content:space-between}
.nav-group{display:flex}
.nav-group a{display:flex;align-items:center;padding:0 17px;height:60px;font-family:"PT Sans Narrow","Arial Narrow",sans-serif;font-weight:700;font-size:21px;color:var(--ink);text-decoration:none;text-transform:uppercase;border-right:1px solid #c98f12}
.nav-group.right a{border-right:none;border-left:1px solid #c98f12}
.nav-group.left a:last-child{border-right:none}
.nav-group.right a:first-child{border-left:none}
.brand-mark{left:522px;top:30px;width:156px;height:156px;background:var(--gold);border:6px solid var(--navy);display:flex;align-items:center;justify-content:center;font-family:"PT Sans Narrow","Arial Narrow",sans-serif;font-weight:700;font-size:64px;color:var(--navy)}
.slider{left:91px;top:151px;width:1018px;height:416px;background:radial-gradient(ellipse at 55% 45%,#7a6030 0%,#3d2e12 55%,#1a1308 100%)}
.slider-arrow{top:297px}
.player{left:159px;top:458px;width:252px;height:64px;border-radius:5px;background:linear-gradient(#3a3a3a,#1c1c1c);border:1px solid #555;display:flex;align-items:center;padding:0 10px;gap:12px}
.player-cover{width:38px;height:38px;background:#8a8a8a;border:1px solid #ccc}
.player-info{flex:1;color:#ddd;font-size:11px;line-height:1.4}
.player-info small{color:#888;font-size:10px}
.player-bar{height:3px;background:#555;margin-top:6px;width:120px;position:relative}
.player-bar i{position:absolute;left:0;top:0;height:3px;width:70%;background:#3aa0d8}
.slider-dots{left:573px;top:544px;display:flex;gap:5px}
.slider-dots span{width:10px;height:10px;border-radius:50%;background:#fff}

/* video gallery */
.section-title{font-size:25px}
.video-grid{left:91px;top:641px;width:1020px;display:grid;grid-template-columns:repeat(4,245px);column-gap:14px;row-gap:16px}
.video-card{height:242px;background:linear-gradient(#fafafa,#e6e6e6);border:1px solid #d2d2d2}
.video-thumb{height:145px;display:flex;align-items:center;justify-content:center}
.play-icon{width:44px;height:44px}
.card-body{padding:14px 14px 0}
.card-title{font-size:18px;color:var(--ink);font-weight:400}
.card-text{font-size:11.5px;line-height:1.55;color:var(--muted);margin-top:4px}

/* photo gallery */
.photo-band{left:0;top:1197px;width:1200px;height:426px;background:var(--gold)}
.photo-feature{left:91px;top:1287px;width:353px;height:260px;background:linear-gradient(135deg,#6b4a30 0%,#c79d6e 55%,#3a2a20 100%)}
.photo-grid{left:452px;top:1287px;width:657px;display:grid;grid-template-columns:repeat(4,159px);gap:7px}
.photo-grid div{height:126px}

/* merchandise */
.merch-band{left:0;top:1623px;width:1200px;height:395px;background:var(--white)}
.merch-grid{left:91px;top:1703px;width:1022px;display:grid;grid-template-columns:repeat(4,246px);column-gap:14px}
.merch-image{height:135px}
.merch-title{font-size:18px;color:var(--ink);margin-top:16px}
.merch-text{font-size:11.5px;line-height:1.55;color:var(--muted);margin-top:2px;padding-right:28px}
.merch-buy{display:flex;align-items:center;gap:18px;margin-top:12px}
.price{font-size:24px;font-weight:600;color:var(--price)}
.btn{background:var(--gold);font-family:"PT Sans Narrow","Arial Narrow",sans-serif;font-weight:700;font-size:17px;color:var(--ink);padding:5px 11px;text-transform:uppercase}

/* footer */
.site-footer{left:0;top:2018px;width:1200px;height:309px;background:linear-gradient(var(--footer-top),var(--footer-bottom))}
.footer-col{top:2060px}
.footer-col h3{font-size:24px;color:var(--white);margin-bottom:14px}
.footer-col li{list-style:none;font-size:12.5px;color:#e4e6f0;line-height:24px}
.footer-note{font-size:12.5px;color:#e4e6f0;margin-bottom:12px}
.field{width:230px;height:30px;border:1px solid #6b77a8;background:#1d2656;color:#dfe2ee;font-size:12px;padding:6px 12px;margin-bottom:8px}
.social{display:flex;gap:6px}
.social span{width:28px;height:28px;border-radius:50%;background:var(--white)}
.footer-base{left:0;top:2327px;width:1200px;height:60px;background:var(--footer-base);border-top:1px solid #2e3a70;color:#9aa2c4;font-size:12.5px;padding:20px 0 0 102px}
</style>
</head>
<body>

<div class="abs hero-backdrop" role="img" aria-label="Warm golden photograph of ornate cathedral arches"></div>
<div class="abs slider" role="img" aria-label="Photograph of the singer performing on a stage under warm spotlights"></div>
<svg class="abs slider-arrow" style="left:118px" width="46" height="100" viewBox="0 0 46 100"><polyline points="44,2 2,50 44,98" fill="none" stroke="#fff" stroke-width="2"/></svg>
<svg class="abs slider-arrow" style="left:1044px" width="46" height="100" viewBox="0 0 46 100"><polyline points="2,2 44,50 2,98" fill="none" stroke="#fff" stroke-width="2"/></svg>

<div class="abs player">
  <div class="player-cover" role="img" aria-label="Album cover"></div>
  <div class="player-info">Quiet Road<br><small>Ashvale</small><div class="player-bar"><i></i></div></div>
  <svg width="62" height="18" viewBox="0 0 62 18" fill="#ddd"><rect x="0" y="4" width="2" height="10"/><polygon points="12,4 3,9 12,14"/><polygon points="26,1 40,9 26,17"/><polygon points="50,4 59,9 50,14"/><rect x="60" y="4" width="2" height="10"/></svg>
</div>
<div class="abs slider-dots"><span></span><span></span><span></span><span></span></div>

<nav class="abs main-nav">
  <div class="nav-group left"><a>Home</a><a>Events</a><a>Music</a><a>Discography</a></div>
  <div class="nav-group right"><a>Pictures</a><a>About</a><a>Video</a><a>Contact</a></div>
</nav>
<div class="abs brand-mark">LH</div>

<h2 class="abs heading section-title" style="left:91px;top:600px">Video Gallery</h2>
<div class="abs video-grid">
  <div class="video-card"><div class="video-thumb" style="background:linear-gradient(135deg,#6a5a4a,#b33a2a)" role="img" aria-label="Video still of the singer in a red dress"><svg class="play-icon" viewBox="0 0 44 44"><circle cx="22" cy="22" r="19" fill="rgba(0,0,0,.45)" stroke="#fff" stroke-width="3"/><polygon points="17,13 31,22 17,31" fill="#fff"/></svg></div><div class="card-body"><div class="card-title">Mauris vel lacus</div><p class="card-text">Morbi diam mauris, viverra in, gravida eu mattis in ante Morbi eget arcu.</p></div></div>
  <div class="video-card"><div class="video-thumb" style="background:linear-gradient(135deg,#3a1030,#a02050)" role="img" aria-label="Video still of a duet on a purple-lit stage"><svg class="play-icon" viewBox="0 0 44 44"><circle cx="22" cy="22" r="19" fill="rgba(0,0,0,.45)" stroke="#fff" stroke-width="3"/><polygon points="17,13 31,22 17,31" fill="#fff"/></svg></div><div class="card-body"><div class="card-title">Mauris vel lacus</div><p class="card-text">Morbi diam mauris, viverra in, gravida eu mattis in ante Morbi eget arcu.</p></div></div>
  <div class="video-card"><div class="video-thumb" style="background:linear-gradient(135deg,#5a2010,#c0502a)" role="img" aria-label="Video still of the singer in warm orange light"><svg class="play-icon" viewBox="0 0 44 44"><circle cx="22" cy="22" r="19" fill="rgba(0,0,0,.45)" stroke="#fff" stroke-width="3"/><polygon points="17,13 31,22 17,31" fill="#fff"/></svg></div><div class="card-body"><div class="card-title">Mauris vel lacus</div><p class="card-text">Morbi diam mauris, viverra in, gravida eu mattis in ante Morbi eget arcu.</p></div></div>
  <div class="video-card"><div class="video-thumb" style="background:linear-gradient(135deg,#4a2a3a,#9a6a6a)" role="img" aria-label="Video still of two singers sharing a microphone"><svg class="play-icon" viewBox="0 0 44 44"><circle cx="22" cy="22" r="19" fill="rgba(0,0,0,.45)" stroke="#fff" stroke-width="3"/><polygon points="17,13 31,22 17,31" fill="#fff"/></svg></div><div class="card-body"><div class="card-title">Mauris vel lacus</div><p class="card-text">Morbi diam mauris, viverra in, gravida eu mattis in ante Morbi eget arcu.</p></div></div>
  <div class="video-card"><div class="video-thumb" style="background:linear-gradient(135deg,#1a2030,#4a5a70)" role="img" aria-label="Video still of the singer before a dark curtain"><svg class="play-icon" viewBox="0 0 44 44"><circle cx="22" cy="22" r="19" fill="rgba(0,0,0,.45)" stroke="#fff" stroke-width="3"/><polygon points="17,13 31,22 17,31" fill="#fff"/></svg></div><div class="card-body"><div class="card-title">Mauris vel lacus</div><p class="card-text">Morbi diam mauris, viverra in, gravida eu mattis in ante Morbi eget arcu.</p></div></div>
  <div class="video-card"><div class="video-thumb" style="background:linear-gradient(135deg,#10306a,#3a80d0)" role="img" aria-label="Video still of a band on a blue-lit stage"><svg class="play-icon" viewBox="0 0 44 44"><circle cx="22" cy="22" r="19" fill="rgba(0,0,0,.45)" stroke="#fff" stroke-width="3"/><polygon points="17,13 31,22 17,31" fill="#fff"/></svg></div><div class="card-body"><div class="card-title">Mauris vel lacus</div><p class="card-text">Morbi diam mauris, viverra in, gravida eu mattis in ante Morbi eget arcu.</p></div></div>
  <div class="video-card"><div class="video-thumb" style="background:linear-gradient(135deg,#3a2a1a,#a07040)" role="img" aria-label="Video still of the singer in a sequined dress"><svg class="play-icon" viewBox="0 0 44 44"><circle cx="22" cy="22" r="19" fill="rgba(0,0,0,.45)" stroke="#fff" stroke-width="3"/><polygon points="17,13 31,22 17,31" fill="#fff"/></svg></div><div class="card-body"><div class="card-title">Mauris vel lacus</div><p class="card-text">Morbi diam mauris, viverra in, gravida eu mattis in ante Morbi eget arcu.</p></div></div>
  <div class="video-card"><div class="video-thumb" style="background:linear-gradient(135deg,#8a7a6a,#3a2a20)" role="img" aria-label="Video still of the singer speaking to camera indoors"><svg class="play-icon" viewBox="0 0 44 44"><circle cx="22" cy="22" r="19" fill="rgba(0,0,0,.45)" stroke="#fff" stroke-width="3"/><polygon points="17,13 31,22 17,31" fill="#fff"/></svg></div><div class="card-body"><div class="card-title">Mauris vel lacus</div><p class="card-text">Morbi diam mauris, viverra in, gravida eu mattis in ante Morbi eget arcu.</p></div></div>
</div>

<div class="abs photo-band"></div>
<h2 class="abs heading section-title" style="left:91px;top:1243px">Photo Gallery</h2>
<div class="abs photo-feature" role="img" aria-label="Portrait photograph of the singer with a fur collar"></div>
<svg class="abs" style="left:100px;top:1393px" width="24" height="48" viewBox="0 0 24 48"><polyline points="22,2 2,24 22,46" fill="none" stroke="#fff" stroke-width="3"/></svg>
<svg class="abs" style="left:410px;top:1393px" width="24" height="48" viewBox="0 0 24 48"><polyline points="2,2 22,24 2,46" fill="none" stroke="#fff" stroke-width="3"/></svg>
<div class="abs photo-grid">
  <div style="background:linear-gradient(135deg,#2a3aa0,#a04ab0)" role="img" aria-label="Photo of the singer singing under blue light"></div>
  <div style="background:linear-gradient(135deg,#5a2a20,#b04a3a)" role="img" aria-label="Photo of the singer in a red gown"></div>
  <div style="background:linear-gradient(135deg,#3a2a20,#a08060)" role="img" aria-label="Photo of the singer with a guest"></div>
  <div style="background:linear-gradient(135deg,#8a8aa0,#c8c8d8)" role="img" aria-label="Photo of the singer on stage with a microphone"></div>
  <div style="background:linear-gradient(135deg,#1a1a1a,#7a7a7a)" role="img" aria-label="Black and white photo of the singer performing"></div>
  <div style="background:linear-gradient(135deg,#c09020,#5a3a10)" role="img" aria-label="Photo of the singer wearing a gold scarf"></div>
  <div style="background:linear-gradient(135deg,#2a1a14,#a07050)" role="img" aria-label="Album cover portrait of the singer"></div>
  <div style="background:linear-gradient(135deg,#10205a,#4a6ac0)" role="img" aria-label="Photo of dancers on a blue stage"></div>
</div>

<div class="abs merch-band"></div>
<h2 class="abs heading section-title" style="left:91px;top:1660px">Purchase Merchandise</h2>
<svg class="abs" style="left:1073px;top:1674px" width="30" height="18" viewBox="0 0 30 18"><polyline points="9,2 2,9 9,16" fill="none" stroke="#999" stroke-width="1.5"/><polyline points="21,2 28,9 21,16" fill="none" stroke="#999" stroke-width="1.5"/></svg>
<div class="abs merch-grid">
  <div><div class="merch-image" style="background:linear-gradient(135deg,#1a1a1a,#8a8a8a)" role="img" aria-label="Black and white concert photo"></div><div class="merch-title">Mauris vel lacus</div><p class="merch-text">Morbi diam mauris, viverra in, gravida eu mattis in ante Morbi eget arcu.</p><div class="merch-buy"><span class="price">$366.99</span><span class="btn">Add to cart</span></div></div>
  <div><div class="merch-image" style="background:linear-gradient(135deg,#a02a6a,#e0a0c0)" role="img" aria-label="Photo of the singer on a pink stage"></div><div class="merch-title">Mauris vel lacus</div><p class="merch-text">Morbi diam mauris, viverra in, gravida eu mattis in ante Morbi eget arcu.</p><div class="merch-buy"><span class="price">$366.99</span><span class="btn">Add to cart</span></div></div>
  <div><div class="merch-image" style="background:linear-gradient(135deg,#10306a,#c05a2a)" role="img" aria-label="Photo of performers on a blue-lit stage"></div><div class="merch-title">Mauris vel lacus</div><p class="merch-text">Morbi diam mauris, viverra in, gravida eu mattis in ante Morbi eget arcu.</p><div class="merch-buy"><span class="price">$366.99</span><span class="btn">Add to cart</span></div></div>
  <div><div class="merch-image" style="background:linear-gradient(135deg,#2a1a14,#7a90b0)" role="img" aria-label="Photo of the singer in a blue dress"></div><div class="merch-title">Mauris vel lacus</div><p class="merch-text">Morbi diam mauris, viverra in, gravida eu mattis in ante Morbi eget arcu.</p><div class="merch-buy"><span class="price">$366.99</span><span class="btn">Add to cart</span></div></div>
</div>

<footer>
  <div class="abs site-footer"></div>
  <div class="abs footer-col" style="left:99px"><h3 class="heading">Quick Links</h3><ul><li>Donec scelerisque</li><li>Lo ac risus</li><li>Praesent sit amet</li><li>Dictum dolor</li><li>Eu dictum porttitor</li><li>Enim felis viverra</li></ul></div>
  <div class="abs footer-col" style="left:311px;top:2064px"><h3 class="heading">Support</h3><ul><li>Donec scelerisque</li><li>Lo ac risus</li><li>Praesent sit amet</li><li>Dictum dolor</li><li>Eu dictum porttitor</li><li>Enim felis viverra</li></ul></div>
  <div class="abs footer-col" style="left:511px;top:2064px"><h3 class="heading">Newsletter Subscribe</h3><p class="footer-note">Please subscribe here for latest offers.</p><div class="field">Your name</div><div class="field">Email address</div><span class="btn" style="display:inline-block;margin-left:137px;margin-top:4px;font-size:15px;padding:4px 12px">Subscribe</span></div>
  <div class="abs footer-col" style="left:839px;top:2064px"><h3 class="heading">Get in Touch</h3><div class="social" aria-label="Social links"><span></span><span></span><span></span><span></span></div></div>
  <div class="abs footer-base">© 2013 Company Name. All right reserved</div>
</footer>

</body>
</html>
```